Q R Ventral Harbor Works, LLC
I just posted pic to use....
where we can find the details for this project....can u upload it in pdf format...so we can start designing it..
Sorry looking for a Trifold brochure

```html
<!DOCTYPE html>
<html lang="en">
<head>
<meta charset="utf-8">
<title>Q R Ventral Harbor Works, LLC – Trifold Brochure</title>
<link href="https://fonts.googleapis.com/css2?family=Arimo:wght@400;700&display=swap" rel="stylesheet">
<style>
  :root{
    --navy:#0a1836;
    --navy-deep:#060f24;
    --blue:#1f5fb8;
    --orange:#f28a1a;
    --orange-light:#f6a640;
    --white:#ffffff;
    --ink:#2a2a2a;
    --soft:#c9d3e6;
  }
  *{box-sizing:border-box;margin:0;padding:0}
  html,body{width:1200px;height:953px;overflow:hidden;background:#fff}
  body{font-family:"Arimo",Arial,sans-serif;}
  .brochure{display:flex;width:1200px;height:953px}
  .panel{position:relative;width:400px;height:953px;overflow:hidden}
  .panel--dark{background:linear-gradient(180deg,var(--navy) 0%,var(--navy-deep) 100%);color:var(--white)}
  .panel--light{background:var(--white);color:var(--ink)}
  .panel + .panel{border-left:1px solid #d8d8d8}
  .hero{position:absolute;left:0;top:0;width:400px}
  .swoosh{position:absolute;left:0;width:400px}
  .content{position:absolute;left:26px;right:26px}
  h2{color:var(--orange);font-size:17px;font-weight:700;margin-bottom:8px}
  h3{color:var(--orange);font-size:12px;font-weight:700;margin:8px 0 3px}
  p,li{font-size:9.6px;line-height:1.38}
  p{margin-bottom:7px}
  ul{margin:0 0 7px 14px}
  li{margin-bottom:2px}
  li strong{color:var(--orange-light)}
  .lead{font-weight:700;color:var(--orange-light)}
  .service{display:flex;flex-direction:column}
  .service-image{width:150px;height:92px;border-radius:2px;margin:8px 0 2px}
  .panel--light h3{font-size:13px}
  .panel--light p{color:#333}
</style>
</head>
<body>
<main class="brochure">

  <!-- Panel 1 : About Us -->
  <section class="panel panel--dark">
    <div class="hero" style="height:220px;background:#fff">
      <div role="img" aria-label="Business people standing on rising blocks" style="width:400px;height:220px;background:linear-gradient(180deg,#ffffff 0%,#eef1f6 55%,#b9c3d3 100%)"></div>
    </div>
    <svg class="swoosh" style="top:190px" width="400" height="60" viewBox="0 0 400 60" aria-hidden="true">
      <path d="M0 20 Q200 60 400 10 L400 60 L0 60Z" fill="#0a1836"/>
      <path d="M0 24 Q200 58 400 14" stroke="#f28a1a" stroke-width="4" fill="none"/>
      <path d="M0 32 Q200 62 400 22" stroke="#1f5fb8" stroke-width="2" fill="none"/>
    </svg>
    <div class="content" style="top:236px">
      <h2>About Us</h2>
      <p class="lead">Q R Ventral Harbor Works, LLC:<br>Outstanding Experience</p>
      <p>Q R Ventral Harbor Works, LLC was founded by Pelcrow Ardent and Lena Marsh. We are a human capital consulting firm dedicated to one thing: helping our clients grow and solve difficult problems related to shifts in performance or just a need of outside support. We deliver fundamental, sustainable improvement through our full range of strategic human resources, administration and management solutions. <strong>Our services include:</strong></p>
      <ul>
        <li><strong>Strategic Implementation and Change:</strong> Improving your organization's flexibility in adapting to a changing business environment.</li>
        <li><strong>Leadership Development:</strong> Giving employees the opportunity and support they need to perform at optimal levels.</li>
        <li><strong>Business &amp; Organization Transformation:</strong> Developing and operating the most effective organization to achieve your mission and objectives.</li>
        <li><strong>Operations &amp; Technology Construction:</strong> Improve the effectiveness of technology initiatives by operational strategies within the organization.</li>
        <li><strong>Business Start-Up Support:</strong> Reduce complexity through simplified service processes that are aligned with customer strategic objectives.</li>
      </ul>
      <p>We advise companies how to attract, develop, engage, and reward their people to attain operating success. We act as a trusted advisor to management, utilizing our broad-level strategic experience to achieve key outcomes that impact culture change. Our goal at all times, regardless of the service, is to find ways to improve outcomes, increase efficiency and increase your profits.</p>
      <p>We are committed to helping our clients find new ideas to solve their most difficult challenges and create lasting value. Along the way, we are not afraid to raise bold questions and have difficult conversations to drive our client's agenda. For us, innovation means continually finding ways to better serve our clients. By doing so, we help organizations develop an enhanced business infrastructure. Our commitment is to provide our clients with strategic solutions that have unparalleled value in the marketplace. Encourage you to explore our website and to contact us to learn more about our unique approach to consulting management.</p>
    </div>
  </section>

  <!-- Panel 2 : Mission -->
  <section class="panel panel--dark">
    <div class="hero" style="height:260px;background:#fff">
      <div role="img" aria-label="Chess pieces on a board, one king standing apart" style="width:400px;height:260px;background:linear-gradient(180deg,#ffffff 0%,#e3e3e3 60%,#8c8c8c 100%)"></div>
    </div>
    <svg class="swoosh" style="top:230px" width="400" height="60" viewBox="0 0 400 60" aria-hidden="true">
      <path d="M0 10 Q200 60 400 20 L400 60 L0 60Z" fill="#0a1836"/>
      <path d="M0 14 Q200 58 400 24" stroke="#f28a1a" stroke-width="4" fill="none"/>
      <path d="M0 22 Q200 62 400 32" stroke="#1f5fb8" stroke-width="2" fill="none"/>
    </svg>
    <div class="content" style="top:276px">
      <h2>Our Mission and Philosophy</h2>
      <p>Q R Ventral Harbor Works' purpose mission is to help solve complex human capital challenges for both public and private organizations. Our goal is to provide quality services needed to address a range of organizational and training opportunities. We facilitate and drive our clients' operation and advance their mission while mitigating risk.</p>
      <h3>Solutions That Show Growth</h3>
      <p>No matter which network partners we draw on, you will be dealing with the Q R Ventral Harbor Works Group people you know, trust and are comfortable with. We deliver skillful strategic innovation solutions backed by accountability. We work in deep partnership with our clients, viewing their successes as our own. Working together, we create better outcomes than either of us could alone.</p>
      <p>Q R Ventral Harbor Works Group does not believe in standard industry answers. We know that custom solutions yield the greatest competitive advantage and value for our clients. We ground each solution in how our client's organization actually works and in the client's unique position in the marketplace.</p>
      <p>In collaboration with each client, we develop new insights about the business, mobilize the organization to act, drive tangible bottom-line results, and make the client organization more effective.</p>
      <h3>What Distinguishes Q R Ventral Harbor Works from the rest?</h3>
      <p>We evaluate our client's strategy, and then help company leaders devise effective approaches to build employees' and customers' emotional engagement. We work to ensure the solutions we recommend produce measurable results that directly tie to business outcomes. Our programs are financially quantifiable, and we will help show they yield an exponential return on investment.</p>
      <p>We identify variation in performance down to the local level. We pinpoint where outstanding performance – and underperformance – is occurring, then guide management in using this knowledge to reduce variation in performance across the organization.</p>
      <p>Contact us today to set up a complimentary consultation.</p>
    </div>
  </section>

  <!-- Panel 3 : Services -->
  <section class="panel panel--light">
    <div class="hero" style="height:190px">
      <div role="img" aria-label="Colourful figures gathered around a central target" style="width:400px;height:190px;background:radial-gradient(circle at 55% 55%,#f4b23a 0%,#e95a4a 25%,#5aa6de 48%,#ffffff 72%)"></div>
    </div>
    <svg class="swoosh" style="top:168px" width="400" height="40" viewBox="0 0 400 40" aria-hidden="true">
      <path d="M0 30 Q200 0 400 26" stroke="#f28a1a" stroke-width="4" fill="none"/>
      <path d="M0 36 Q200 6 400 32" stroke="#1f5fb8" stroke-width="2" fill="none"/>
    </svg>
    <div class="content" style="top:212px">
      <h2>Our Services</h2>
      <p>We offer services in all areas of business management to companies of all sizes in a wide variety of industries. Some of our important practice areas are listed below.</p>
      <div class="service">
        <h3>Planning and Management</h3>
        <p>Whether your company requires short-term or long-term resources, our expert advice will help you navigate safely into your corporate future.</p>
        <div class="service-image" role="img" aria-label="Interlocking puzzle pieces" style="background:linear-gradient(135deg,#f0f0f0,#b8bcc4)"></div>
      </div>
      <div class="service">
        <h3>Program Management</h3>
        <p>We combine our consulting expertise to help with the implementation of a strategic management process tightly coupled with project management to convert strategic opportunity to project results.</p>
        <div class="service-image" role="img" aria-label="Hands placing orange directional arrows" style="background:linear-gradient(135deg,#fbe1bd,#e98a2a)"></div>
      </div>
      <div class="service">
        <h3>Compliance and Logistic Management</h3>
        <p>There are risks involved in any business. We provide you with extensive and personal advice before a crisis hits.</p>
        <div class="service-image" role="img" aria-label="Network of connected figures" style="height:70px;background:linear-gradient(135deg,#dfe9f5,#6f95c7)"></div>
      </div>
      <div class="service">
        <h3>Information Technology</h3>
        <p>Our information technology services focus on advising and building upon existing business practices as well as design and implementation of start-ups.</p>
      </div>
    </div>
  </section>

</main>
</body>
</html>
```